Design and Format this paper into a Info Deck

I need the attached PowerPoint "Lorvenst" to be created into a verticle, printable information deck. Normal size for print.

This document will be a tool for my sales team to provide additional science-based information about our ingredient "ClearVita Algaeblend"

Use attached Whitelabel-onesheet pdf for style/font comparable

Add:
Cover page with "Marisel Harvest" logo (main company)
Title: ClearVita Algaeblend Science (with "ClearVita" logo)

Changes:
Replace "Lorvenst" logo everywhere with ClearVita logo

Add all notes in powerpoint into the on-screen page as text. Can make design a side-by-side two page to fit all text & graphics.

```html
<!DOCTYPE html>
<html lang="en">
<head>
<meta charset="utf-8">
<title>ClearVita Algaeblend Science – Info Deck</title>
<link href="https://fonts.googleapis.com/css2?family=Catamaran:wght@400;500;600;700&display=swap" rel="stylesheet">
<style>
  :root{
    --backdrop:#707070;
    --paper:#f7f7f6;
    --paper-shade:#e9ecea;
    --ink:#232323;
    --ink-soft:#3a3a3a;
    --green-deep:#127238;
    --green:#23913d;
    --green-head:#2f9a3f;
    --lime:#8dc63f;
    --lime-soft:#a9cf5a;
    --tag:#cfdca0;
    --organ-a:#c0643e;
    --organ-b:#e3b27a;
    --vessel-a:#b3212a;
    --vessel-b:#e7a0a0;
  }
  *{box-sizing:border-box;margin:0;padding:0}
  html,body{width:1200px;height:819px;overflow:hidden}
  body{background:var(--backdrop);font-family:"Catamaran",sans-serif;color:var(--ink);position:relative}

  .spread{position:absolute;display:flex;box-shadow:0 2px 6px rgba(0,0,0,.35)}
  .page{position:relative;height:100%;overflow:hidden;
        background:linear-gradient(160deg,#ffffff 0%,var(--paper) 45%,var(--paper-shade) 100%)}
  .page + .page{box-shadow:inset 6px 0 8px -6px rgba(0,0,0,.25)}
  .arrows{position:absolute;left:0;top:0;pointer-events:none}

  .rule{position:absolute;height:0;border-top:.6px solid var(--green)}
  .kicker{position:absolute;font-size:8.6px;font-weight:700;font-style:italic;color:var(--green-deep);letter-spacing:-.1px}
  .heading{position:absolute;font-size:10.2px;font-weight:500;color:var(--green-head);line-height:1.2}
  .heading u{text-decoration-thickness:.6px;text-underline-offset:1.5px}
  .title-dark{position:absolute;font-size:11.4px;font-weight:600;color:var(--ink);line-height:1.05;text-transform:uppercase}

  .node{position:absolute;font-size:6.6px;line-height:1.18;color:var(--ink);white-space:nowrap}
  .node b{font-weight:600}
  .node .ref{display:block;font-size:4.9px;margin-top:1.5px;color:var(--ink-soft)}
  .node.c{transform:translateX(-50%);text-align:center}
  .node.r{transform:translateX(-100%);text-align:right}
  .label{position:absolute;font-size:5px;color:var(--ink)}

  .brand{position:absolute;font-size:10.4px;font-weight:700;color:var(--green);white-space:nowrap;transform:translateX(-50%);letter-spacing:-.1px}

  .figure{position:absolute;border-radius:3px}
  .figure.organ{background:linear-gradient(135deg,var(--organ-a),var(--organ-b))}
  .figure.vessel{background:linear-gradient(90deg,var(--vessel-a),var(--vessel-b))}

  .tag{position:absolute;background:var(--tag);font-size:5.6px;font-style:italic;text-align:center;line-height:1;display:flex;align-items:center;justify-content:center;color:var(--ink)}
  .panel-text{position:absolute;font-size:6.4px;line-height:1.2}
  .panel-text .ref{display:block;font-size:4.9px;margin-top:2px}

  .notes{position:absolute;font-size:3.7px;line-height:1.32;color:var(--ink)}
  .notes p{margin-bottom:1.6px}
  .notes ul{padding-left:6px}
  .glossary{position:absolute;font-size:3.75px;line-height:1.36;color:var(--ink);text-align:left}
  .glossary p{margin-bottom:2px}
  .refs{position:absolute;font-size:4.6px;color:var(--ink)}
  .refs h4{font-weight:600;font-size:4.6px;margin-bottom:5px}

  .band{position:absolute;left:0;right:0;bottom:0;background:linear-gradient(90deg,var(--green-deep) 0%,var(--green) 45%,var(--lime) 100%)}
  .band-brand{position:absolute;font-size:7.4px;font-weight:600;color:#fff;white-space:nowrap}

  .cover{position:absolute;background:linear-gradient(170deg,#ffffff 0%,#f6f7f5 60%,#eef1ee 100%);box-shadow:0 2px 6px rgba(0,0,0,.35);overflow:hidden}
  .cover-title{position:absolute;left:25px;top:295px;font-size:12px;font-weight:700;color:var(--green);white-space:nowrap;letter-spacing:-.1px}
  .cover-company{position:absolute;right:14px;bottom:8px;font-size:7.4px;font-weight:600;color:#fff;white-space:nowrap}
</style>
</head>
<body>

<!-- Spread: hypolipidemic -->
<section class="spread" style="left:44px;top:47px;width:556px;height:358px">
  <article class="page" style="width:278px">
    <div class="rule" style="left:16px;top:15px;width:243px"></div>
    <div class="kicker" style="left:16px;top:22px">IN VIVO TESTING</div>
    <h2 class="heading" style="left:16px;top:35px">Demonstrated <u>hypolipidemic</u> effects in animal models</h2>

    <div class="node r" style="left:79px;top:57px">Decrease in<br>total cholesterol<span class="ref">Varel et al., 2019</span></div>
    <div class="figure organ" role="img" aria-label="Illustration of a pancreas" style="left:144px;top:63px;width:28px;height:14px"></div>
    <div class="label" style="left:146px;top:83px">Pancreas</div>
    <div class="figure organ" role="img" aria-label="Illustration of a liver" style="left:111px;top:79px;width:28px;height:18px"></div>
    <div class="label" style="left:112px;top:100px">Liver</div>
    <div class="figure organ" role="img" aria-label="Illustration of adipose tissue" style="left:140px;top:97px;width:17px;height:17px"></div>
    <div class="label" style="left:159px;top:99px;line-height:1.1">Adipose<br>tissue</div>
    <div class="node" style="left:214px;top:81px">Increase in<br>LPL activity<span class="ref">Varel et al., 2019</span></div>
    <div class="node r" style="left:79px;top:107px">Decrease in<br>triglycerides<span class="ref">Varel et al., 2019<br>Kelvane-Durat<br>et al., 2019</span></div>

    <div class="brand" style="left:138px;top:145px">ClearVita Algaeblend</div>

    <div class="node r" style="left:79px;top:168px">Decrease in<br>VLDL-C &amp; LDL-C<span class="ref">Varel et al., 2019</span></div>
    <div class="figure vessel" role="img" aria-label="Illustration of a blood vessel with red blood cells" style="left:89px;top:205px;width:35px;height:15px"></div>
    <div class="label" style="left:103px;top:224px">Plasma</div>
    <div class="figure organ" role="img" aria-label="Illustration of a liver" style="left:176px;top:206px;width:28px;height:18px"></div>
    <div class="label" style="left:176px;top:228px">Liver</div>
    <div class="node" style="left:210px;top:206px">Decrease in<br>fat content<span class="ref">Ostrand et al., 2022</span></div>

    <div class="node r" style="left:79px;top:246px">Increase in<br>HDL-C<span class="ref">Varel et al., 2019<br>Ostrand et al., 2022</span></div>
    <div class="node c" style="left:110px;top:251px">Decrease in<br>triglycerides<span class="ref">Varel et al., 2020</span></div>
    <div class="node" style="left:140px;top:246px">Decrease in<br>cholesterol<span class="ref">Varel et al., 2020</span></div>

    <div class="rule" style="left:16px;top:281px;width:243px;border-color:#9a9a9a"></div>
    <div class="notes" style="left:16px;top:287px;width:118px">
      <p><b>HDL-C</b>: high density lipoprotein-colesterol</p>
      <p><b>LPL</b>: Lipoprotein lipase is an enzyme that degrades circulating triglycerides in the bloodstream. These triglycerides are embedded in very low-density lipoproteins (VLDL) and chylomicrons traveling through the bloodstream.</p>
    </div>
    <div class="notes" style="left:137px;top:287px;width:122px">
      <p>Fatty acids liberated from the triglycerides are then used for storage in adipose tissue or fuel in skeletal or cardiac muscle.</p>
      <p><b>LDL-C</b>: low density lipoprotein-cholesterol</p>
      <p><b>VLDL-C</b>: very low density lipoprotein-colesterol</p>
    </div>
    <div class="band" style="height:30px"></div>
  </article>

  <article class="page" style="width:278px">
    <div class="rule" style="left:10px;top:15px;width:244px"></div>
    <div class="kicker" style="left:10px;top:22px">IN VIVO TESTING</div>
    <h2 class="heading" style="left:10px;top:35px">Demonstrated <u>hypolipidemic</u> effects in animal models</h2>
    <div class="brand" style="left:129px;top:58px">ClearVita Algaeblend</div>
    <div class="figure vessel" role="img" aria-label="Illustration of a blood vessel with red blood cells" style="left:107px;top:107px;width:46px;height:23px"></div>
    <div class="label" style="left:123px;top:137px">Plasma (P)</div>
    <div class="node r" style="left:84px;top:139px">Decrease in<br>glucose levels<span class="ref">Varel et al., 2019<br>Varel et al., 2020<br>Ostrand et al., 2022<br>Kelvane-Durat<br>et al., 2019</span></div>
    <div class="node" style="left:185px;top:139px">Decrease in<br>glycated hemoglobin<span class="ref">Varel et al., 2019<br>Varel et al., 2020</span></div>

    <div class="rule" style="left:10px;top:199px;width:244px;border-color:#555"></div>
    <div class="kicker" style="left:10px;top:207px">IN VIVO TESTING</div>
    <h2 class="heading" style="left:10px;top:219px;width:230px">Demonstrated <u>hepatoprotective</u> effects in animal models</h2>
    <div class="node c" style="left:137px;top:256px;font-size:6.9px">Decrease in serum levels of ALT, AST, ALP, and LDH</div>
    <div class="node r" style="left:222px;top:266px;font-size:6.4px">Varel, 2020</div>

    <div class="rule" style="left:10px;top:281px;width:244px;border-color:#9a9a9a"></div>
    <div class="notes" style="left:8px;top:287px;width:122px">
      <ul>
        <li>Glycated hemoglobin has always been considered as an important indicator of long-term glycemic control. The excess glucose present in the blood reacts with hemoglobin to form glycated hemoglobin.</li>
        <li>Serum alanine aminotransferase (ALT), aspartate amino-transferase (AST), alkaline phosphatase ALP, lactate</li>
      </ul>
    </div>
    <div class="notes" style="left:134px;top:287px;width:120px">
      <p>dehydrogenase LDH. High levels of these enzymes is attributed to the leakage of the enzymes from the liver cytosol into the bloodstream, which may be due to liver dysfunction or damage of liver cells.</p>
    </div>
    <div class="band" style="height:30px"></div>
    <div class="band-brand" style="left:207px;top:333px">Marisel Harvest</div>
  </article>

  <svg class="arrows" width="556" height="358" viewBox="0 0 556 358" aria-hidden="true">
    <defs>
      <marker id="head-thick" viewBox="0 0 10 10" refX="5" refY="5" markerWidth="2.6" markerHeight="2.6" orient="auto"><path d="M0 0 L10 5 L0 10 z" fill="#1d8a3b"/></marker>
      <marker id="head-thin" viewBox="0 0 10 10" refX="5" refY="5" markerWidth="5" markerHeight="5" orient="auto"><path d="M0 1 L10 5 L0 9 z" fill="#93c447"/></marker>
    </defs>
    <g stroke="#93c447" stroke-width=".9" fill="none" marker-end="url(#head-thin)">
      <line x1="103" y1="88" x2="91" y2="75"/>
      <line x1="103" y1="98" x2="91" y2="111"/>
      <line x1="186" y1="90" x2="205" y2="90"/>
      <line x1="79" y1="213" x2="69" y2="203"/>
      <line x1="79" y1="230" x2="69" y2="240"/>
      <line x1="108" y1="234" x2="108" y2="245"/>
      <line x1="131" y1="230" x2="142" y2="240"/>
      <line x1="376" y1="124" x2="365" y2="135"/>
      <line x1="443" y1="124" x2="455" y2="135"/>
    </g>
    <g stroke="#1d8a3b" stroke-width="3" fill="none" marker-end="url(#head-thick)">
      <line x1="138" y1="139" x2="138" y2="122"/>
      <line x1="122" y1="182" x2="110" y2="195"/>
      <line x1="154" y1="182" x2="166" y2="195"/>
      <line x1="407" y1="79" x2="407" y2="97"/>
    </g>
  </svg>
</section>

<!-- Spread: anti-inflammatory & anti-proliferative -->
<section class="spread" style="left:621px;top:47px;width:551px;height:355px">
  <article class="page" style="width:278px">
    <div class="rule" style="left:16px;top:15px;width:243px"></div>
    <div class="kicker" style="left:16px;top:22px">IN VIVO AND IN VITRO TESTING</div>
    <h2 class="heading" style="left:16px;top:35px">Demonstrated <u>anti-inflammatory</u> effect</h2>
    <div class="brand" style="left:136px;top:101px">ClearVita Algaeblend</div>
    <div class="tag" style="left:45px;top:144px;width:82px;height:15px">In vivo<br>(animal model)</div>
    <div class="tag" style="left:146px;top:144px;width:81px;height:15px">In vitro</div>
    <div class="panel-text" style="left:45px;top:165px">Decrease in serum levels<br>of IL-6 and TNFα<span class="ref">Ostrand et al., 2022</span></div>
    <div class="panel-text" style="left:146px;top:165px">Inhibited production of<br>TNFα induced by LPS dif-<br>ferentiated macrophages<span class="ref">del Amaro et al., 2014</span></div>
    <div class="rule" style="left:16px;top:274px;width:243px;border-color:#9a9a9a"></div>
    <div class="notes" style="left:16px;top:280px;width:120px">
      <p>IL-6, Interleukin 6</p>
      <p>TNFα, Tumor Necrosis Factor alpha</p>
      <p>IL-6 and TNFα are two of the major pro-inflammatory cytokines</p>
    </div>
    <div class="band" style="height:31px"></div>
  </article>

  <article class="page" style="width:273px">
    <div class="rule" style="left:10px;top:15px;width:253px"></div>
    <div class="kicker" style="left:10px;top:22px">IN VITRO TESTING</div>
    <h2 class="heading" style="left:10px;top:35px">Demonstrated <u>anti-proliferative</u> effect in tumor cells</h2>
    <div class="node c" style="left:133px;top:80px">Caco-2<br>(human colorectal<br>adenocarcinoma)<span class="ref">Serrat-Vidal et al., 2021</span></div>
    <div class="node c" style="left:47px;top:117px">UACC-62<br>(human skin melanoma)<span class="ref">Olmeda-Ruiz et al., 2016</span></div>
    <div class="node c" style="left:220px;top:106px">A549<br>(adenocarcinomic<br>human alveolar<br>basal epithelial cells)<span class="ref">Ostrand et al., 2022</span></div>
    <div class="brand" style="left:133px;top:172px">ClearVita Algaeblend</div>
    <div class="node c" style="left:47px;top:197px">HepG2<br>(human liver cancer)<span class="ref">Serrat-Vidal et al., 2021</span></div>
    <div class="node c" style="left:220px;top:198px">HT-29<br>(human colon cancer)<span class="ref">Olmeda-Ruiz et al., 2016</span></div>
    <div class="node c" style="left:97px;top:252px">HCT-116<br>(human colon cancer)<span class="ref">Tallis and Brenn, 2016</span></div>
    <div class="node c" style="left:171px;top:251px">T84<br>(human colorectal<br>carcinoma)<span class="ref">Ostrand et al., 2022</span></div>
    <div class="band" style="height:31px"></div>
    <div class="band-brand" style="left:203px;top:328px">Marisel Harvest</div>
  </article>

  <svg class="arrows" width="551" height="355" viewBox="0 0 551 355" aria-hidden="true">
    <defs>
      <marker id="head-lime" viewBox="0 0 10 10" refX="5" refY="5" markerWidth="5" markerHeight="5" orient="auto"><path d="M0 1 L10 5 L0 9 z" fill="#93c447"/></marker>
      <marker id="head-green" viewBox="0 0 10 10" refX="5" refY="5" markerWidth="5" markerHeight="5" orient="auto"><path d="M0 1 L10 5 L0 9 z" fill="#1d8a3b"/></marker>
    </defs>
    <g stroke="#1d8a3b" stroke-width=".9" marker-end="url(#head-green)">
      <line x1="104" y1="123" x2="94" y2="135"/>
      <line x1="168" y1="123" x2="180" y2="135"/>
    </g>
    <g stroke="#93c447" stroke-width=".9" marker-end="url(#head-lime)">
      <line x1="411" y1="166" x2="411" y2="114"/>
      <line x1="391" y1="170" x2="355" y2="143"/>
      <line x1="431" y1="170" x2="467" y2="143"/>
      <line x1="368" y1="199" x2="343" y2="202"/>
      <line x1="453" y1="199" x2="478" y2="202"/>
      <line x1="403" y1="199" x2="384" y2="245"/>
      <line x1="416" y1="199" x2="438" y2="247"/>
    </g>
  </svg>
</section>

<!-- Spread: other bioactivities & glossary -->
<section class="spread" style="left:47px;top:429px;width:548px;height:355px">
  <article class="page" style="width:276px">
    <div class="rule" style="left:16px;top:16px;width:243px"></div>
    <h2 class="title-dark" style="left:16px;top:28px;width:250px">Other potential bioactivies exhibited by in vitro testing</h2>
    <div class="node c" style="left:141px;top:56px"><b>Skin protection against<br>oxidative damage</b><br>Increased cell viability under<br>oxidative stress in NHDF cells<span class="ref">Pramsey et al., 2017</span></div>
    <div class="node c" style="left:56px;top:98px"><b>Anti-steatotic effect</b><br>Prevented accumulation of<br>triglycerides induced by palmitic<br>acid in cultured hepatocytes<br>(AML-12 cells)<span class="ref">Ferrell-Quint et al., 2023</span></div>
    <div class="node c" style="left:225px;top:104px"><b>Anti-hypertensive effect</b><br>Inhibition of ACE-1<span class="ref">del Amaro et al., 2014</span></div>
    <div class="brand" style="left:137px;top:162px">ClearVita Algaeblend</div>
    <div class="node c" style="left:61px;top:193px"><b>Antioxidant effect</b><br>Up-regulation of GPX1 and<br>FOXO3 genes in NHDF cells<span class="ref">Pramsey et al., 2017</span></div>
    <div class="node c" style="left:219px;top:193px"><b>Immunomodulatory effect</b><br>Up-regulation of FOXO3 and<br>KLF2 genes in NHDF cells<span class="ref">Pramsey et al., 2017</span></div>
    <div class="node c" style="left:88px;top:240px"><b>Anti-inflammatory effect</b><br>Up-regulation of FOXO3, KLF2,<br>and IL-1R genes in NHDF cells<span class="ref">Pramsey et al., 2017</span></div>
    <div class="node c" style="left:189px;top:240px"><b>Anti-adipogenic effect</b><br>Up-regulation of KLF2 gene in<br>NHDF cells<span class="ref">Pramsey et al., 2017</span></div>
    <div class="rule" style="left:16px;top:281px;width:243px;border-color:#9a9a9a"></div>
    <div class="notes" style="left:16px;top:286px;width:108px">
      <p><b>NHDF</b>: Normal Human Dermal Fibroblasts</p>
      <p><b>ACE-1</b> is a key enzyme that helps to regulate the salt-water balance and blood pressure within the renin-angiotensin-aldosterone system. It converts Ang-I in</p>
    </div>
    <div class="notes" style="left:143px;top:286px;width:116px">
      <p>Ang-II, which is considered the main active peptide, which acts on target tissues and regulates blood pressure through renal reabsorption of sodium and water and systemic vasoconstriction.</p>
    </div>
    <div class="band" style="height:30px"></div>
  </article>

  <article class="page" style="width:272px">
    <div class="rule" style="left:13px;top:16px;width:255px"></div>
    <div class="glossary" style="left:13px;top:28px;width:121px">
      <p><b>Glutathione peroxidases</b> are a family of enzymes that uses glutathione as a co-substrate in the reduction of H<sub>2</sub>O<sub>2</sub> to water. Glutathione peroxidase-1 (GPX1) is the most abundant member of the family and is considered a crucial in preventing the harmful accumulation of intracellular H<sub>2</sub>O<sub>2</sub>.</p>
      <p><b>FOX</b>: Forkhead box proteins are transcriptional regulators that play a key role in the modulation of a range of cellular biological processes including substrate metabolism, protein turnover, cell survival and proliferation, cell death, autophagy, inflammation, cytokine expression, and immunity. In particular, a role of FOXO subfamily in the cellular strategies of antioxidant defense is well established. FOXO3 is a representative member of the FOXO subfamily, which is expressed in a range of different tissues, and can be regulated at different levels: transcription, translation, and post-translational modifications. FOXO3 is known to protect cells from oxidative stress by directly increasing the manganese superoxide dismutase isoform (MnSOD, or SOD2) both at transcriptional and protein levels. Additional studies have shown that FOXO3 is also required for the expression of not only SOD2 but also other key antioxidant genes such as SOD1, catalase (CAT), and GPX1. On the other hand, it is known that perturbations in the expression or activity of FOXO3 are increasingly linked to chronic inflammatory processes. Anti-inflammatory and immunomodulatory actions of FOXO3 are well characterized, and include: i) inhibition of production of inflammatory cytokines such as IL-2 and IL-6, ii) a critical role for T-cell proliferation and activation, monocyte cytokine secretion, or neutrophil survival, and it can also direct inflammatory response in non-immune cells, and iii) limitation of memory T cells expansion.</p>
      <p><b>KLF</b>: The Krüppel-like family of DNA-binding transcription factors (a total of 17 different members, referred to as KLF1 to KLF17, have been characterized so far) have been found in all multicellular organisms, where they control a broad range of intracellular processes including quiescence, proliferation, differentiation, development, growth and inflammation. Among them, KLF2 has been detected in a range of different tissues, including spleen, thymus, adipose tissue, skeletal muscle, heart, as well as in myeloid and lymphoid immune cells. According to literature, it is known that KLF2 plays key roles in: i) immune function, regulating survival, migration and trafficking of T-cells and B-cells, controlling proliferation of induced regulatory T-cells, and regulating activation, differentiation, and cytokine secretion in monocytes, ii) inflammation, acting as an inhibitor of NF-kB, a well-known transcription factor that plays a central role in regulation of inflammation mediating pro-inflammatory signals (Halvik, 2020), and iii) adipogenesis, through inhibition of peroxisome proliferator-activated receptor-g (PPAR-g) expression.</p>
    </div>
    <div class="refs" style="left:146px;top:29px">
      <h4>REFERENCE LIST</h4>
      <p>[ References to be inserted here ]</p>
    </div>
    <div class="band" style="height:30px"></div>
    <div class="band-brand" style="left:204px;top:332px">Marisel Harvest</div>
  </article>

  <svg class="arrows" width="548" height="355" viewBox="0 0 548 355" aria-hidden="true">
    <defs>
      <marker id="head-lime-3" viewBox="0 0 10 10" refX="5" refY="5" markerWidth="5" markerHeight="5" orient="auto"><path d="M0 1 L10 5 L0 9 z" fill="#93c447"/></marker>
    </defs>
    <g stroke="#a9cf5a" stroke-width=".9" marker-end="url(#head-lime-3)">
      <line x1="137" y1="158" x2="137" y2="103"/>
      <line x1="116" y1="157" x2="83" y2="129"/>
      <line x1="159" y1="157" x2="192" y2="129"/>
      <line x1="92" y1="184" x2="72" y2="188"/>
      <line x1="182" y1="184" x2="204" y2="188"/>
      <line x1="131" y1="185" x2="111" y2="233"/>
      <line x1="144" y1="185" x2="165" y2="233"/>
    </g>
  </svg>
</section>

<!-- Cover -->
<section class="cover" style="left:624px;top:431px;width:275px;height:355px">
  <h1 class="cover-title">ClearVita Algaeblend Science</h1>
  <svg width="275" height="355" viewBox="0 0 275 355" style="position:absolute;left:0;top:0" aria-hidden="true">
    <defs>
      <linearGradient id="cover-wave" x1="0" y1="0" x2="1" y2="0">
        <stop offset="0" stop-color="#127238"/>
        <stop offset=".6" stop-color="#1f8a3b"/>
        <stop offset="1" stop-color="#2e9a3f"/>
      </linearGradient>
      <linearGradient id="cover-wave-light" x1="0" y1="0" x2="1" y2="0">
        <stop offset="0" stop-color="#8dc63f"/>
        <stop offset="1" stop-color="#5fb043"/>
      </linearGradient>
    </defs>
    <path d="M0 326 C70 308 170 320 275 274 L275 355 L0 355 Z" fill="url(#cover-wave-light)" opacity=".7"/>
    <path d="M0 332 C80 316 180 328 275 287 L275 355 L0 355 Z" fill="url(#cover-wave)"/>
    <path d="M0 328 C80 312 180 324 275 282" fill="none" stroke="#ffffff" stroke-width="1.2"/>
  </svg>
  <div class="cover-company">Marisel Harvest</div>
</section>

</body>
</html>
```